Create a Business Card Design Project for a new logistics company

We need a business card designed for a new company in Australia.

Type of business is logistics/trucking.

Medium will be brushed black metal card that can/will be acid etched to a brushed steel silver, acid die cut and two printed colours of our choice which will be white and pantone orange.

We have hopes that the design will be simple, modern and represent with a quick glance what our company does.

Please read instructions carefully in must have box any questions please ask.

If you are interested in this job please look at other job that we have which is very similar with logo and design

Please have a look at the things that can be done with metals cards on google images for inspiration.

Target Market(s)

Men from 20yrs of age to 60yrs of age

Industry/Entity Type

Steel

Requirements
Must have
• Must Have:
- Front of card:

Must use the company logo and name provided as attachment (see below KVR-black-background-cmyk).
Logo grey will be etched, orange and white will be printed on card. Parts of the logo could even be die cut.

The word -Logistics anytime, anywhere- on front etched, printed or die cut.

detail needed on front or back depending on your design layout.

Name
position
email
mobile

all details can be on front if a nice design is etched on the back of card or to keep front simple you can put all detail on back of card, I will leave the lay out to you.

Colours in logo are

Pantone 144 C Orange
Pantone 11-0601 White
Pantone 7539 C Gray
Pantone 426 C Black

However black will be the base of black metal card. Gray will be replaced with the etching in card revealing the silver. Orange and white will be printed on card.

have fun!!
Nice to have
• The file attached called idea is just an example of what can be designed and etched into card. Google has many more idea's for metal business cards.
Should not have
• Please don't clutter the card
No fonts smaller then 7 points

```html
<!DOCTYPE html>
<html lang="en">
<head>
<meta charset="utf-8">
<title>KVR Industries – Business Card</title>
<link rel="stylesheet" href="https://fonts.googleapis.com/css2?family=Nunito:wght@400;600;700&display=swap">
<style>
  :root {
    --stage: #e6e4e1;
    --card-black: #1b1e21;
    --card-edge: #2a2d31;
    --brand-orange: #f7941d;
    --text-light: #d9d9d9;
    --text-muted: #b9b9b9;
    --icon-grey: #c4c4c4;
    --etch-copper: #8a5a3c;
    --etch-dark: #2b221d;
  }
  * { margin: 0; padding: 0; box-sizing: border-box; }
  html, body {
    width: 1200px;
    height: 598px;
    overflow: hidden;
    background: var(--stage);
    font-family: "Nunito", sans-serif;
  }
  .business-card {
    position: absolute;
    left: 290px;
    top: 118px;
    width: 610px;
    height: 348px;
    background: var(--card-black);
    border: 1px solid var(--card-edge);
    border-radius: 6px;
    overflow: hidden;
  }
  .brand {
    position: absolute;
    left: 26px;
    top: 40px;
    display: flex;
    align-items: center;
    gap: 16px;
  }
  .brand-mark {
    width: 46px;
    height: 46px;
    border-radius: 50%;
    background: var(--brand-orange);
  }
  .brand-name {
    font-weight: 700;
    font-size: 36px;
    letter-spacing: 1px;
    line-height: 1;
    color: var(--brand-orange);
  }
  .tagline {
    position: absolute;
    left: 108px;
    top: 92px;
    font-size: 19px;
    font-weight: 600;
    letter-spacing: 0.3px;
    color: var(--text-light);
  }
  .holder-name {
    position: absolute;
    left: 27px;
    top: 150px;
    font-size: 23px;
    font-weight: 700;
    color: var(--text-light);
  }
  .holder-position {
    position: absolute;
    left: 27px;
    top: 184px;
    font-size: 14px;
    font-weight: 600;
    color: var(--text-muted);
  }
  .contact-list {
    position: absolute;
    left: 25px;
    top: 232px;
    list-style: none;
  }
  .contact-item {
    display: flex;
    align-items: center;
    height: 28px;
    font-size: 16px;
    font-weight: 600;
    letter-spacing: 0.6px;
    color: var(--text-light);
  }
  .contact-icon {
    width: 24px;
    height: 22px;
    margin-right: 13px;
    fill: none;
    stroke: var(--icon-grey);
    stroke-width: 1.6;
  }
  .etched-feature {
    position: absolute;
    left: 300px;
    top: 72px;
    width: 310px;
    height: 276px;
    background: radial-gradient(ellipse at 70% 55%, var(--etch-copper) 0%, var(--etch-dark) 60%, var(--card-black) 100%);
    border-top-left-radius: 60% 80%;
    opacity: 0.85;
  }
</style>
</head>
<body>
  <main class="business-card">
    <div class="brand">
      <span class="brand-mark"></span>
      <span class="brand-name">KVR INDUSTRIES</span>
    </div>
    <p class="tagline">Logistics anytime, anywhere</p>

    <div class="etched-feature" role="img" aria-label="Perforated copper etched decoration"></div>

    <h1 class="holder-name">Your name</h1>
    <p class="holder-position">Position</p>

    <ul class="contact-list">
      <li class="contact-item">
        <svg class="contact-icon" viewBox="0 0 24 22" aria-hidden="true">
          <rect x="7" y="1.5" width="10" height="19" rx="1.5" transform="rotate(40 12 11)"/>
        </svg>
        (012) 555 - 6789
      </li>
      <li class="contact-item">
        <svg class="contact-icon" viewBox="0 0 24 22" aria-hidden="true">
          <rect x="2" y="5" width="20" height="13" rx="1"/>
          <path d="M2 5 L12 13 L22 5"/>
        </svg>
        yourname@kvrfreight.com
      </li>
      <li class="contact-item">
        <svg class="contact-icon" viewBox="0 0 24 22" aria-hidden="true">
          <circle cx="12" cy="11" r="9.5"/>
          <ellipse cx="12" cy="11" rx="4" ry="9.5"/>
          <path d="M2.5 11 H21.5 M4 6 H20 M4 16 H20"/>
        </svg>
        www.kvrfreight.com
      </li>
    </ul>
  </main>
</body>
</html>
```